Lantern Motion for Neighbors Business Cards

I need business cards for staff in a new startup. Our company name is Movrela - we train Tai Chi teachers. But our biggest project is called Lantern Motion for Neighbors - a federal project to put together free Tai Chi classes for Vets all across America. It's a young company, with a spirit of excitement, passion, a desire to do good for others (our Vets) and a modern style and sensibility. In other words, not old-fashioned Asian martial arts theme, but something new.

Industry/Entity Type

Health And Wellness

Contact Information for Business Card

The topic is ancient healing, but the company is the Pembrooks - so I'd like a card design that captures that.

Font styles to use
Sans Serif

Colors

Designer to choose colors to be used in the design.

Requirements
Nice to have
• I've got two logos - one for the company and one for the project. I want to see if we can incorporate them both without it becoming too busy.
Should not have
• Overly old-fashioned yin-yang themes.

```html
<!DOCTYPE html>
<html lang="en">
<head>
<meta charset="UTF-8">
<title>Lantern Motion for Neighbors – Business Cards</title>
<link href="https://fonts.googleapis.com/css2?family=Josefin+Sans:wght@400;600&display=swap" rel="stylesheet">
<style>
  :root {
    --stage: #23262b;
    --card-white: #ffffff;
    --card-red: #d9313d;
    --card-red-deep: #b81f2b;
    --card-black: #141414;
    --gold: #e7b96a;
    --brand-red: #c8202a;
  }
  * { margin: 0; padding: 0; box-sizing: border-box; }
  html, body {
    width: 1200px; height: 900px; overflow: hidden;
    background: var(--stage);
    font-family: "Josefin Sans", sans-serif;
  }
  .stage { position: relative; width: 1200px; height: 900px; }

  /* Front card */
  .card-front {
    position: absolute; left: 150px; top: 190px;
    width: 330px; height: 520px;
    border-radius: 30px; overflow: hidden;
    background: linear-gradient(180deg, var(--card-red) 0%, var(--card-red-deep) 100%);
    box-shadow: 0 18px 40px rgba(0,0,0,.45);
  }
  .card-front .top-band {
    position: absolute; left: 0; top: 0; width: 330px; height: 230px;
  }
  .brand-name {
    position: absolute; left: 0; top: 76px; width: 330px;
    text-align: center;
    font-size: 30px; font-weight: 600; color: var(--brand-red);
    letter-spacing: 1px;
  }
  .contact {
    position: absolute; right: 30px; top: 290px;
    text-align: right; color: var(--gold);
  }
  .person-name {
    font-size: 24px; font-weight: 600; letter-spacing: 3px;
    text-transform: uppercase; margin-bottom: 30px;
  }
  .contact-row {
    display: flex; justify-content: flex-end; align-items: center; gap: 10px;
    font-size: 15px; line-height: 1.3; margin-bottom: 16px;
  }
  .contact-row .address { font-size: 19px; line-height: 1.2; }
  .icon { width: 22px; height: 22px; flex: none; }

  /* Back card */
  .card-back {
    position: absolute; left: 560px; top: 250px;
    width: 500px; height: 310px;
    border-radius: 26px;
    background: radial-gradient(ellipse at 40% 30%, #222 0%, var(--card-black) 70%);
    box-shadow: 0 18px 40px rgba(0,0,0,.5);
    display: flex; align-items: center; justify-content: center;
    padding: 0 40px;
  }
  .project-name {
    color: var(--gold);
    font-size: 26px; font-weight: 400; letter-spacing: 1px;
    white-space: nowrap;
  }
</style>
</head>
<body>
<main class="stage">

  <section class="card-front" aria-label="Business card front">
    <svg class="top-band" viewBox="0 0 330 230" aria-hidden="true">
      <path d="M0 0 H330 V150 C280 215 110 240 0 205 Z" fill="var(--card-white)"/>
    </svg>
    <p class="brand-name">Movrela</p>
    <div class="contact">
      <p class="person-name">Jordan Vale</p>
      <div class="contact-row">
        <span class="address">Stree, State<br>Country</span>
        <svg class="icon" viewBox="0 0 24 24" aria-hidden="true">
          <path d="M12 2a7 7 0 0 0-7 7c0 5 7 13 7 13s7-8 7-13a7 7 0 0 0-7-7zm0 9.5A2.5 2.5 0 1 1 12 6.5a2.5 2.5 0 0 1 0 5z" fill="var(--gold)"/>
        </svg>
      </div>
      <div class="contact-row">
        <span>+00 123 456</span>
        <svg class="icon" viewBox="0 0 24 24" aria-hidden="true">
          <circle cx="12" cy="12" r="11" fill="var(--card-red-deep)"/>
          <path d="M8.5 6.5l2 2-1.2 1.4c.7 1.6 2 2.9 3.6 3.6l1.4-1.2 2 2-1.5 1.7c-3.8-.4-7.6-4.2-8-8z" fill="var(--card-white)"/>
        </svg>
      </div>
      <div class="contact-row">
        <span>jordan.vale@movrela.org</span>
        <svg class="icon" viewBox="0 0 24 24" aria-hidden="true">
          <circle cx="12" cy="12" r="11" fill="var(--card-white)"/>
          <rect x="6.5" y="8" width="11" height="8" rx="1" fill="none" stroke="var(--card-red-deep)" stroke-width="1.5"/>
          <path d="M6.5 8.5l5.5 4 5.5-4" fill="none" stroke="var(--card-red-deep)" stroke-width="1.5"/>
        </svg>
      </div>
    </div>
  </section>

  <section class="card-back" aria-label="Business card back">
    <p class="project-name">Lantern Motion for Neighbors</p>
  </section>

</main>
</body>
</html>
```